依頼詳細
写真・ビデオの撮影・編集および写真スタジオを行っています。お客様にお送りする封筒のデザインをお願いします。かっこよく・爽やかなイメージでお願いします。封筒の下位置部分のレイアウトでお願いします。。
記載項目
法人名/住所/電話/Fax/ホームページアドレス+ロゴ
希望イメージ
シンプル 複雑
単色 カラフル
暗い 明るい
日常 高級
遊び心 厳粛
未来的 伝統的
女性的 男性的
希望する色
青系、水色系、緑系
納品ファイル
• フォトショップ形式 (.psd)
補足説明
素材のロゴデータのロゴ部分と文字部分のバランスはおまかせ致します。
封筒の色は白色で考えております。よろしくお願い致します。

```html
<!DOCTYPE html>
<html lang="ja">
<head>
<meta charset="utf-8">
<title>封筒デザイン</title>
<link rel="stylesheet" href="https://fonts.googleapis.com/css2?family=Montserrat:wght@600&family=Noto+Sans+JP:wght@400;500&display=swap">
<style>
  :root {
    --aqua: #6cc6cd;
    --paper: #ffffff;
    --ink: #333333;
    --edge: #c9c9c9;
    --postal-red: #e0303a;
  }
  html, body {
    margin: 0;
    padding: 0;
    overflow: hidden;
    background: var(--paper);
  }
  .envelope {
    position: relative;
    width: 796px;
    height: 1200px;
    box-sizing: border-box;
    border: 2px solid var(--edge);
    background: var(--paper);
    font-family: "Noto Sans JP", sans-serif;
    color: var(--ink);
    overflow: hidden;
  }
  .flap {
    position: absolute;
    left: 0; top: 0;
    width: 100%;
    height: 128px;
    background: var(--aqua);
    display: flex;
    align-items: center;
    justify-content: center;
  }
  .flap-name {
    font-family: "Montserrat", sans-serif;
    font-weight: 600;
    font-size: 40px;
    letter-spacing: 4px;
    color: var(--paper);
    transform: rotate(180deg);
  }
  .postal-boxes {
    position: absolute;
    left: 540px;
    top: 198px;
  }
  .sender {
    position: absolute;
    left: 118px;
    top: 910px;
  }
  .brand {
    display: flex;
    align-items: center;
    gap: 12px;
    font-family: "Montserrat", sans-serif;
    font-weight: 600;
    font-size: 44px;
    letter-spacing: 3px;
    color: var(--ink);
    line-height: 1;
  }
  .brand-mark {
    width: 22px;
    height: 22px;
    background: var(--aqua);
  }
  .brand-bar {
    margin-top: 16px;
    width: 310px;
    height: 24px;
    background: var(--aqua);
  }
  .details {
    margin-top: 18px;
    font-size: 16px;
    line-height: 36px;
    letter-spacing: 0.5px;
  }
  .details p { margin: 0; }
  .details .company { font-weight: 500; }
  .details .url { color: var(--aqua); }
</style>
</head>
<body>
  <div class="envelope">
    <div class="flap"><span class="flap-name">LUMINA</span></div>

    <svg class="postal-boxes" width="236" height="40" viewBox="0 0 236 40" aria-label="郵便番号枠">
      <g fill="none" stroke="var(--postal-red)">
        <rect x="1.5" y="1.5" width="26" height="36" stroke-width="3"/>
        <rect x="33.5" y="1.5" width="26" height="36" stroke-width="3"/>
        <rect x="65.5" y="1.5" width="26" height="36" stroke-width="3"/>
        <line x1="93" y1="20" x2="103" y2="20" stroke-width="2"/>
        <rect x="104.5" y="1.5" width="26" height="36" stroke-width="1.5"/>
        <rect x="137.5" y="1.5" width="26" height="36" stroke-width="1.5"/>
        <rect x="170.5" y="1.5" width="26" height="36" stroke-width="1.5"/>
        <rect x="203.5" y="1.5" width="26" height="36" stroke-width="1.5"/>
      </g>
    </svg>

    <div class="sender">
      <div class="brand"><span class="brand-mark"></span>LUMINA</div>
      <div class="brand-bar"></div>
      <div class="details">
        <p class="company">株式会社ルミナスタジオ</p>
        <p>〒530-0012　大阪府青葉市緑ヶ丘町8-21</p>
        <p>TEL:06-4820-7725 / FAX:06-4820-7726</p>
        <p class="url">https://lumina-studio.jp/</p>
      </div>
    </div>
  </div>
</body>
</html>
```